Real Estate Investment Opportunity needs a print and web brochure

need a porfessional looking information brochure to present and describe the investment opportunity.
This is an introductory brochure AND a take away brochure from investment meetings.
Ideally it will be easy to amend content and edit after.
Preliminary content is drafted, some photos are available.
Once the layout is completed the brochure will need to be translated into FRENCH (canadian), so it is available in both official languages of Canada. If you are capable of proper translating, that is a plus, but if not - translated text can be provided later
This assignment could also be done in power point.
medium to high net worth individuals
Investment

```html
<!DOCTYPE html>
<html lang="en">
<head>
<meta charset="utf-8">
<title>Salaberry-de-Valleyfield – Market Profile</title>
<link href="https://fonts.googleapis.com/css2?family=Gelasio:wght@400&display=swap" rel="stylesheet">
<style>
  :root {
    --page-bg: #ffffff;
    --page-edge: #9a9a9a;
    --ink: #1e1e1e;
    --header-ink: #555555;
    --accent-teal: #3aa9c4;
    --accent-brown: #4a3a12;
    --panel-navy: #0c2a63;
    --panel-text: #ffffff;
    --bullet: #3aa9c4;
    --photo-sky: #6ea8dc;
    --photo-mid: #8fb2c9;
    --photo-water: #2f5f95;
  }
  * { margin: 0; padding: 0; box-sizing: border-box; }
  html, body {
    width: 903px; height: 1200px; overflow: hidden;
    background: var(--page-bg);
  }
  .page {
    position: relative; width: 903px; height: 1200px;
    border: 1.5px solid var(--page-edge);
    font-family: "Gelasio", Georgia, serif;
    color: var(--ink);
  }
  .running-head {
    position: absolute; top: 62px; right: 52px;
    display: flex; align-items: center;
    font-size: 12px; letter-spacing: 0.6px; color: var(--header-ink);
  }
  .running-head .page-number {
    margin-left: 8px; padding-left: 7px;
    border-left: 2px solid var(--header-ink); line-height: 16px;
  }
  .rule { position: absolute; top: 159px; height: 12px; }
  .rule--teal { left: 2px; width: 344px; background: var(--accent-teal); }
  .rule--brown { left: 352px; right: 0; background: var(--accent-brown); }
  .hero-photo {
    position: absolute; left: 2px; top: 179px; width: 446px; height: 399px;
    background: linear-gradient(180deg, var(--photo-sky) 0%, #a9c9e6 38%, var(--photo-mid) 55%, var(--photo-water) 100%);
  }
  .title-panel {
    position: absolute; left: 452px; top: 179px; right: 0; height: 399px;
    background: var(--panel-navy);
  }
  .title-panel svg { position: absolute; left: 0; top: 170px; }
  .title-panel h1 {
    position: absolute; left: 31px; top: 176px;
    font-weight: 400; font-size: 33px; color: var(--panel-text);
    white-space: nowrap;
  }
  .intro {
    position: absolute; left: 96px; top: 601px;
    font-size: 17px; line-height: 28.8px; white-space: nowrap;
  }
  .facts {
    position: absolute; left: 84px; top: 826px;
    list-style: none; font-size: 17px; line-height: 29.6px; white-space: nowrap;
  }
  .facts li::before {
    content: "*"; color: var(--bullet); font-size: 19px; margin-right: 2px;
  }
</style>
</head>
<body>
<div class="page">
  <header class="running-head">
    <span class="brand">LES RÉSIDENCES HORIZON</span>
    <span class="page-number">10</span>
  </header>

  <div class="rule rule--teal"></div>
  <div class="rule rule--brown"></div>

  <div class="hero-photo" role="img" aria-label="Photo of a cyclist by the waterfront with a red brick mill building and trees under a blue sky"></div>

  <section class="title-panel">
    <svg width="14" height="28" viewBox="0 0 14 28" aria-hidden="true">
      <polygon points="0,0 14,14 0,28" fill="#ffffff"/>
    </svg>
    <h1>Salaberry-de-Valleyfield</h1>
  </section>

  <div class="intro">
    <p>This former mill town remains an industrial centre as well as a comfortable suburb of<br>
    Montreal. Its location near the Ontario and U.S. borders, and not far from the bucolic<br>
    Eastern Townships, the community is a popular place to rent.</p>
    <p>Vacancies dropped 78.3% in 2011 to a stunning 0.5%, even as new construction boosts the<br>
    available rental stock by 2.8%. 1</p>
    <p>Salaberry-de-Valleyfield ranks 17th all agglomerations of Quebec (including Census<br>
    Metropolitan Areas) for the size of its population</p>
    <p>.</p>
  </div>

  <ul class="facts">
    <li>Population: 40,077, but serves a regional population of nearly 200 000 people</li>
    <li>Median age: 44.6 years</li>
    <li>Unemployment Rate: 7.1%</li>
    <li>Number of households: 17,515</li>
    <li>bilingualism rate: 34%</li>
    <li>Base of more than 19,000 workers-residents</li>
    <li>70% of residents are working</li>
    <li>6,155 workers from outside the municipality</li>
    <li>More than 100 manufacturing companies - 3200 jobs</li>
    <li>More than 1,000 companies and business services - 10,000 jobs</li>
    <li>High concentration of jobs in the institutional sector</li>
  </ul>
</div>
</body>
</html>
```